Brightpath Learning Data Dashboard

Brightpath Learning is a leading provider of digital curriculum and online courses to increase educational opportunities and achievement to students in grades K-12. Teachers and students access all course materials online.

School districts need greater visibility into the rate in which students are progressing through their courses, so school staff can better support students to complete courses at the required rate to keep them on track for graduation.
This can be accomplished by allowing school administrators to view a data dashboard and pull an on-demand report and see progress for a specified date range, relative to overall progress.

Within a specified date range, school administrators want to know if the student made more or less progress than in the period prior to the first date in the range.
School administrators also want to know if students are ahead or behind where they should be after the second date in the range.

Industry/Entity Type

Digital

```html
<!DOCTYPE html>
<html lang="en">
<head>
<meta charset="utf-8">
<title>Brightpath Learning – Time Based Performance Report</title>
<link href="https://fonts.googleapis.com/css2?family=Jost:wght@400&family=Roboto:wght@400;500&display=swap" rel="stylesheet">
<style>
:root{
  --page:#f5f5f6;
  --ink:#1b2236;
  --sidebar:#1b2a45;
  --brand:#0f47a8;
  --brand-deep:#0d45a6;
  --filter:#eef3fb;
  --canvas:#dde6f3;
  --button:#1e88e5;
  --text:#3b4250;
  --muted:#9aa3b2;
  --line:#e1e5ec;
  --red:#e5525c;
  --green:#8fcf5a;
  --blue:#4aa8e8;
}
*{box-sizing:border-box;margin:0;padding:0}
html,body{width:1025px;height:1200px;overflow:hidden}
body{background:var(--page);position:relative;font-family:"Roboto",Arial,sans-serif;color:var(--text)}
.title{position:absolute;top:88px;left:0;width:1025px;text-align:center;font-family:"Jost",Arial,sans-serif;font-weight:400;font-size:53px;letter-spacing:1px;color:var(--ink)}
.screen{position:absolute;background:var(--canvas);overflow:hidden}
.sidebar{position:absolute;left:0;top:0;bottom:0;background:var(--sidebar)}
.sidebar svg{position:absolute;left:50%;transform:translateX(-50%)}
.topbar{position:absolute;top:0;right:0;background:var(--brand);color:#fff;display:flex;align-items:center}
.home{border-radius:50%;background:#2a8cf0;display:flex;align-items:center;justify-content:center}
.filters{position:absolute;right:0;background:var(--filter)}
.abs{position:absolute}
.label{position:absolute;color:#555c68}
.field{position:absolute;background:#fff;border-radius:12px;color:#b3b9c4;display:flex;align-items:center}
.field .clear{position:absolute;border-radius:50%;background:#dfe4ec}
.radio{position:absolute;border-radius:50%;border:1px solid #555c68}
.radio.on{border-color:var(--button)}
.radio.on::after{content:"";position:absolute;inset:2px;border-radius:50%;background:var(--button)}
.download{position:absolute;background:var(--button);color:#fff;border-radius:12px;display:flex;align-items:center}
.download .dot{position:absolute;border-radius:50%;background:#fff}
.tab{position:absolute;text-align:center}
.tab.active{color:#222;border-bottom:2px solid var(--button)}
.tab.idle{color:var(--muted)}
table{position:absolute;border-collapse:collapse;background:#fff;table-layout:fixed}
th{background:var(--brand-deep);color:#fff;font-weight:400;text-align:left;vertical-align:top}
td{border-top:1px solid var(--line);white-space:nowrap;overflow:hidden}

/* summary screen */
.summary{left:138px;top:202px;width:738px;height:498px}
.summary .sidebar{width:51px}
.summary .topbar{left:51px;height:42px;font-size:13.5px}
.summary .home{width:20px;height:20px;margin:0 11px 0 21px}
.summary .filters{left:51px;top:42px;height:93px}
.summary .label{font-size:8.5px}
.summary .field{height:20px;font-size:8px;padding-left:10px}
.summary .field .clear{width:14px;height:14px;top:3px;right:4px}
.summary .radio{width:8px;height:8px}
.summary .download{font-size:8.5px;padding-left:16px;height:22px}
.summary .download .dot{width:15px;height:15px;right:4px;top:3.5px}
.summary .tab{font-size:9.5px;height:20px;line-height:16px}
.summary table{left:72px;top:154px;width:645px;font-size:7.6px}
.summary th{height:66px;padding:15px 10px 0;border-left:1px solid rgba(255,255,255,.25);line-height:1.25}
.summary td{height:21px;padding:0 10px;border-left:1px solid var(--line)}

/* performance screen */
.performance{left:244px;top:610px;width:536px;height:330px;box-shadow:0 18px 40px rgba(20,30,60,.25)}
.performance .sidebar{width:35px}
.performance .topbar{left:35px;height:30px;font-size:9.8px}
.performance .home{width:15px;height:15px;margin:0 8px 0 15px}
.performance .filters{left:35px;top:30px;height:70px}
.performance .label{font-size:5.8px}
.performance .field{height:14px;font-size:5.3px;padding-left:7px}
.performance .field .clear{width:10px;height:10px;top:2px;right:3px}
.performance .radio{width:6px;height:6px}
.performance .radio.on::after{inset:1.5px}
.performance .download{font-size:5.6px;padding-left:12px;height:16px;background:#7cbcf2}
.performance .download .dot{width:11px;height:11px;right:3px;top:2.5px}
.performance .tab{font-size:6.8px;height:15px;line-height:12px}
.performance table{left:50px;top:152px;width:472px;font-size:4.8px;text-align:center}
.performance th{padding:3px 4px;border-left:1px solid rgba(255,255,255,.25);line-height:1.2;font-size:4.8px;text-align:center}
.performance th.left{text-align:left;padding-left:7px}
.performance th.band{background:#3b68b8;font-size:4.4px;padding:2px}
.performance td{height:15.4px;padding:0 3px;border-left:1px solid var(--line)}
.performance td.left{text-align:left;padding-left:7px}
.neg{color:var(--red)}
.pill{display:inline-block;background:var(--green);color:#fff;border-radius:5px;padding:1px 5px}
.status{display:inline-block;width:7px;height:7px;border-radius:50%;color:#fff;font-size:6px;line-height:7px;text-align:center}
.status.up{background:var(--green)}
.status.down{background:var(--red)}
.status.even{background:var(--blue)}
</style>
</head>
<body>

<h1 class="title">Brightpath Learning</h1>

<!-- Student Summary screen -->
<section class="screen summary">
  <nav class="sidebar">
    <svg style="top:18px" width="10" height="8"><rect y="0" width="10" height="1.6" fill="#fff"/><rect y="3.2" width="10" height="1.6" fill="#fff"/><rect y="6.4" width="10" height="1.6" fill="#fff"/></svg>
    <svg style="top:61px" width="9" height="9"><path d="M4.5 0 9 4H7.5v5h-6V4H0z" fill="#8a96ad"/></svg>
    <svg style="top:101px" width="9" height="9"><circle cx="4.5" cy="4.5" r="3.7" fill="none" stroke="#8a96ad" stroke-width="1.2"/><circle cx="4.5" cy="4.5" r="1.4" fill="#8a96ad"/></svg>
    <svg style="top:143px" width="9" height="9"><rect width="4" height="5" fill="#8a96ad"/><rect x="5" width="4" height="3" fill="#8a96ad"/><rect y="6" width="4" height="3" fill="#8a96ad"/><rect x="5" y="4" width="4" height="5" fill="#8a96ad"/></svg>
    <svg style="top:184px" width="9" height="9"><rect width="9" height="9" rx="1" fill="#8a96ad"/><rect x="2" y="4" width="1.2" height="3" fill="#1b2a45"/><rect x="4" y="2" width="1.2" height="5" fill="#1b2a45"/><rect x="6" y="5" width="1.2" height="2" fill="#1b2a45"/></svg>
    <svg style="top:225px" width="10" height="8"><path d="M0 3 5 0 10 3v5H0z" fill="#8a96ad"/><path d="M0 3 5 6 10 3" fill="none" stroke="#1b2a45" stroke-width="1"/></svg>
    <svg style="top:266px" width="9" height="9"><rect y="1" width="9" height="8" rx="1" fill="#8a96ad"/><rect x="2" y="4" width="2" height="2" fill="#1b2a45"/></svg>
    <svg style="top:307px" width="10" height="10"><circle cx="5" cy="5" r="3.2" fill="none" stroke="#8a96ad" stroke-width="2.4" stroke-dasharray="2 1.4"/><circle cx="5" cy="5" r="1.3" fill="#8a96ad"/></svg>
  </nav>
  <header class="topbar">
    <span class="home"><svg width="9" height="9"><path d="M4.5 1 8.5 4.5H7v3.5H2V4.5H.5z" fill="#fff"/></svg></span>
    Time Based Performance Report
  </header>
  <div class="filters">
    <span class="label" style="left:31px;top:19px">School:</span>
    <span class="radio on" style="left:179px;top:20px"></span><span class="label" style="left:192px;top:19px">Observer:</span>
    <span class="radio" style="left:240px;top:20px"></span><span class="label" style="left:253px;top:19px">Teacher:</span>
    <span class="label" style="left:327px;top:19px">Date</span>
    <span class="label" style="left:424px;top:19px">Date</span>
    <div class="field" style="left:21px;top:29px;width:132px">Choose a school<span class="clear"></span></div>
    <div class="field" style="left:158px;top:29px;width:153px">Choose an observer ...<span class="clear"></span></div>
    <div class="field" style="left:317px;top:29px;width:89px">From<span class="clear"></span></div>
    <div class="field" style="left:415px;top:29px;width:90px">To<span class="clear"></span></div>
    <div class="download" style="left:557px;top:28px;width:107px">Download Report<span class="dot"></span></div>
    <div class="tab active" style="left:21px;top:71px;width:113px">Student Summary</div>
    <div class="tab idle" style="left:146px;top:71px;width:112px">Student Performance</div>
  </div>
  <table>
    <colgroup><col style="width:82px"><col style="width:82px"><col style="width:92px"><col style="width:91px"><col style="width:75px"><col style="width:75px"><col style="width:73px"><col style="width:75px"></colgroup>
    <thead><tr><th>Students<br>Name</th><th>Observer</th><th>School</th><th>Course<br>Title</th><th>Current<br>Grade</th><th>Raw<br>Score</th><th>Course Start<br>Date</th><th>Course End<br>Date</th></tr></thead>
    <tbody>
      <tr><td>Anthony Jones</td><td>Sam Cox</td><td>Rosemont</td><td>Algebra 1A</td><td>67.3%</td><td>70%</td><td>2/20/18</td><td>4/24/18</td></tr>
      <tr><td>Jose Alvarez</td><td>Sam Cox</td><td>Rosemont</td><td>Biology A</td><td>74.2%</td><td>83%</td><td>2/20/18</td><td>4/24/18</td></tr>
      <tr><td>Maria Lee</td><td>Jema Interiano</td><td>Kennedy</td><td>US History A</td><td>82.3%</td><td>82.3%</td><td>2/20/18</td><td>4/24/18</td></tr>
      <tr><td>Marcus Smith</td><td>Jema Interiano</td><td>Kennedy</td><td>Algebra 1A</td><td>91.0%</td><td>95.0%</td><td>2/20/18</td><td>4/24/18</td></tr>
      <tr><td>Juan Rodriguez</td><td>Meg Johnson</td><td>Burbank</td><td>Language Arts 10 A</td><td>94.5%</td><td>94.5%</td><td>2/20/18</td><td>4/24/18</td></tr>
      <tr><td>Jose Carlos</td><td>Meg Johnson</td><td>Burbank</td><td>Language Arts 10B</td><td>80%</td><td>85%</td><td>2/20/18</td><td>4/24/18</td></tr>
      <tr><td>Julie Carns</td><td>Meg Johnson</td><td>Burbank</td><td>US History 1A</td><td>75%</td><td>80%</td><td>2/20/18</td><td>4/24/18</td></tr>
      <tr><td>Anthony Jones</td><td>Sam Cox</td><td>Rosemont</td><td>Algebra 1A</td><td>67.3%</td><td>70%</td><td>2/20/18</td><td>4/24/18</td></tr>
      <tr><td>Jose Alvarez</td><td>Sam Cox</td><td>Rosemont</td><td>Biology A</td><td>74.2%</td><td>83%</td><td>2/20/18</td><td>4/24/18</td></tr>
      <tr><td>Maria Lee</td><td>Jema Interiano</td><td>Kennedy</td><td>US History A</td><td>82.3%</td><td>82.3%</td><td>2/20/18</td><td>4/24/18</td></tr>
      <tr><td>Marcus Smith</td><td>Jema Interiano</td><td>Kennedy</td><td>Algebra 1A</td><td>91.0%</td><td>95.0%</td><td>2/20/18</td><td>4/24/18</td></tr>
    </tbody>
  </table>
</section>

<!-- Student Performance screen -->
<section class="screen performance">
  <nav class="sidebar">
    <svg style="top:13px" width="7" height="6"><rect width="7" height="1.2" fill="#fff"/><rect y="2.4" width="7" height="1.2" fill="#fff"/><rect y="4.8" width="7" height="1.2" fill="#fff"/></svg>
    <svg style="top:43px" width="6" height="6"><path d="M3 0 6 3H5v3H1V3H0z" fill="#8a96ad"/></svg>
    <svg style="top:73px" width="6" height="6"><circle cx="3" cy="3" r="2.4" fill="none" stroke="#8a96ad"/></svg>
    <svg style="top:103px" width="6" height="6"><rect width="2.6" height="3.4" fill="#8a96ad"/><rect x="3.4" width="2.6" height="2" fill="#8a96ad"/><rect y="4" width="2.6" height="2" fill="#8a96ad"/><rect x="3.4" y="2.6" width="2.6" height="3.4" fill="#8a96ad"/></svg>
    <svg style="top:133px" width="6" height="6"><rect width="6" height="6" rx="1" fill="#8a96ad"/></svg>
    <svg style="top:163px" width="7" height="6"><path d="M0 2 3.5 0 7 2v4H0z" fill="#8a96ad"/></svg>
    <svg style="top:193px" width="6" height="6"><rect y="1" width="6" height="5" rx="1" fill="#8a96ad"/></svg>
    <svg style="top:223px" width="7" height="7"><circle cx="3.5" cy="3.5" r="2.2" fill="none" stroke="#8a96ad" stroke-width="1.8" stroke-dasharray="1.4 1"/></svg>
  </nav>
  <header class="topbar">
    <span class="home"><svg width="7" height="7"><path d="M3.5 .5 6.5 3.5H5.5v3h-4v-3H.5z" fill="#fff"/></svg></span>
    Time Based Performance Report
  </header>
  <div class="filters">
    <span class="label" style="left:24px;top:11px">School:</span>
    <span class="radio on" style="left:132px;top:12px"></span><span class="label" style="left:141px;top:11px">Observer:</span>
    <span class="radio" style="left:180px;top:12px"></span><span class="label" style="left:189px;top:11px">Teacher:</span>
    <span class="label" style="left:244px;top:11px">Date</span>
    <span class="label" style="left:317px;top:11px">Date</span>
    <div class="field" style="left:16px;top:19px;width:100px">Choose a school<span class="clear"></span></div>
    <div class="field" style="left:121px;top:19px;width:112px">Choose an observer<span class="clear"></span></div>
    <div class="field" style="left:238px;top:19px;width:70px">From<span class="clear"></span></div>
    <div class="field" style="left:312px;top:19px;width:70px">To<span class="clear"></span></div>
    <div class="download" style="left:453px;top:18px;width:80px">Download Report<span class="dot"></span></div>
    <div class="tab idle" style="left:22px;top:52px;width:80px">Student Summary</div>
    <div class="tab active" style="left:100px;top:52px;width:84px">Student Performance</div>
  </div>
  <table>
    <colgroup><col style="width:61px"><col style="width:60px"><col style="width:33px"><col style="width:34px"><col style="width:33px"><col style="width:35px"><col style="width:44px"><col style="width:42px"><col style="width:43px"><col style="width:43px"><col style="width:44px"></colgroup>
    <thead>
      <tr><th class="left" rowspan="3" style="vertical-align:top;padding-top:10px">Students<br>Name</th><th class="left" rowspan="3" style="vertical-align:top;padding-top:10px">Observer</th><th colspan="4">Percent Complete</th><th rowspan="3" style="text-align:left;vertical-align:top;padding-top:10px">2/27-3/6<br>Progress<br>Actual/<br>Goal</th><th rowspan="3" style="text-align:left;vertical-align:top;padding-top:10px">Status as<br>of Mar 6</th><th rowspan="3" style="text-align:left;vertical-align:top;padding-top:10px">Completion<br>Rate/day<br>for the<br>range</th><th rowspan="3" style="text-align:left;vertical-align:top;padding-top:10px">Completion<br>Rate<br>Change</th><th rowspan="3" style="text-align:left;vertical-align:top;padding-top:10px">Last<br>Login</th></tr>
      <tr><th class="band" colspan="2">START ~ 2/27/18</th><th class="band" colspan="2">END ~ 3/6/18</th></tr>
      <tr><th>Actual<br>(%)</th><th>Goal<br>(%)</th><th>Actual<br>(%)</th><th>Goal<br>(%)</th></tr>
    </thead>
    <tbody>
      <tr><td class="left">Anthony Jones</td><td class="left">Sam Cox</td><td>0%</td><td>10%</td><td>5%</td><td>20%</td><td class="neg">5/10</td><td class="neg">5/20</td><td>2%</td><td><span class="status up">+</span></td><td>3/6/18</td></tr>
      <tr><td class="left">Jose Alvarez</td><td class="left">Sam Cox</td><td>5%</td><td>10%</td><td>15%</td><td>20%</td><td><span class="pill">10/10</span></td><td class="neg">15/20</td><td>2.28%</td><td><span class="status up">+</span></td><td>3/6/18</td></tr>
      <tr><td class="left">Maria Lee</td><td class="left">Jema Interiano</td><td>15%</td><td>10%</td><td>20%</td><td>20%</td><td class="neg">5/10</td><td><span class="pill">20/20</span></td><td>7.14%</td><td><span class="status up">+</span></td><td>3/6/18</td></tr>
      <tr><td class="left">Marcus Smith</td><td class="left">Jema Interiano</td><td>9%</td><td>10%</td><td>11%</td><td>20%</td><td class="neg">2/10</td><td class="neg">11/20</td><td>5%</td><td><span class="status down">×</span></td><td>3/6/18</td></tr>
      <tr><td class="left">Juan Rodriguez</td><td class="left">Meg Johnson</td><td>11%</td><td>10%</td><td>11%</td><td>20%</td><td class="neg">7/10</td><td class="neg">18/20</td><td>2.8%</td><td><span class="status down">×</span></td><td>3/2/18</td></tr>
      <tr><td class="left">Jose Carlos</td><td class="left">Meg Johnson</td><td>5%</td><td>10%</td><td>28%</td><td>20%</td><td class="neg">5/10</td><td class="neg">10/20</td><td>3%</td><td><span class="status down">×</span></td><td>3/2/18</td></tr>
      <tr><td class="left">Julie Carns</td><td class="left">Meg Johnson</td><td>10%</td><td>10%</td><td>10%</td><td>20%</td><td><span class="pill">10/10</span></td><td><span class="pill">20/20</span></td><td>2%</td><td><span class="status even">=</span><span class="status even">=</span></td><td>3/5/18</td></tr>
      <tr><td class="left">Anthony Jones</td><td class="left">Sam Cox</td><td>0%</td><td>10%</td><td>5%</td><td>20%</td><td class="neg">5/10</td><td class="neg">5/20</td><td>2%</td><td><span class="status up">+</span></td><td>3/6/18</td></tr>
      <tr><td class="left">Jose Alvarez</td><td class="left">Sam Cox</td><td>5%</td><td>10%</td><td>15%</td><td>20%</td><td><span class="pill">10/10</span></td><td class="neg">15/20</td><td>2.28%</td><td><span class="status up">+</span></td><td>3/6/18</td></tr>
      <tr><td class="left">Maria Lee</td><td class="left">Jema Interiano</td><td>15%</td><td>10%</td><td>20%</td><td>20%</td><td class="neg">5/10</td><td><span class="pill">20/20</span></td><td>7.14%</td><td><span class="status up">+</span></td><td>3/6/18</td></tr>
      <tr><td class="left">Anthony Jones</td><td class="left">Meg Johnson</td><td>0%</td><td>0%</td><td>0%</td><td>0%</td><td class="neg">7/10</td><td class="neg">11/20</td><td>3%</td><td><span class="status down">×</span></td><td>3/6/18</td></tr>
    </tbody>
  </table>
</section>

</body>
</html>
```